Marlowvane Services Website Design

We have most content but require a professional design. We have a logo already and will need it utilized along with several of the photos from the attached documentation.
First page should have our mission and Vision and the synapsis provided in the word document. Visitors will be prompted to select from one of our 3 divisions from this page.
Each division will have the same list of tabs : About, Services, Safety, Careers and Contact.
Photos on each divisions page should be representative of the divisions offerings. The word doc attached contains the requested content and we are open to edits that would complement and fill the website.
I like the Tornwick site www.tornwick-example.com - they are our competition so cant be modeled directly after this.
Please include prompts to request quote at each service page. align the format of the geotechnical page to the other 2 divisions.
I used chat gpt for some of the content so will need it optimized for SCO.

```html
<!DOCTYPE html>
<html lang="en">
<head>
<meta charset="utf-8">
<title>Marlowvane Services – Landing Page Mobile View</title>
<link href="https://fonts.googleapis.com/css2?family=Inter:ital,wght@0,400;0,500;0,600;0,700;0,800;1,700;1,800&display=swap" rel="stylesheet">
<style>
  :root{
    --bg:#2b2b30;
    --screen:#2d2d32;
    --red:#ec1c24;
    --deep-red:#8b2327;
    --white:#ffffff;
    --paper:#f4f4f4;
    --ink:#1f1f22;
  }
  *{box-sizing:border-box;margin:0;padding:0}
  html,body{width:1065px;height:1200px;overflow:hidden;background:var(--bg)}
  body{position:relative;font-family:"Inter",Arial,sans-serif;color:var(--white)}

  .board-brand{position:absolute;left:0;width:1100px;top:46px;text-align:center;font-weight:800;font-size:44px;letter-spacing:6px;color:var(--red);line-height:1}
  .board-title{position:absolute;left:0;width:1100px;top:104px;text-align:center;font-weight:700;font-size:27px;color:var(--white)}

  .phone{position:absolute;width:215px;border:4px solid var(--white);border-radius:30px;background:var(--screen);overflow:hidden}
  .phone > *{position:absolute}

  .section-heading{display:flex;align-items:center;justify-content:center;gap:5px;font-weight:500;font-size:14px;letter-spacing:2.4px;color:var(--red);left:0;width:100%;line-height:1}
  .section-heading::before,.section-heading::after{content:"";width:17px;height:1px;background:currentColor}
  .section-heading.light{color:var(--white)}
  .section-heading.start{justify-content:flex-start;padding-left:13px}

  /* Division picker */
  .hero-photo{inset:0;background:linear-gradient(180deg,#6a6a70 0%,#55565b 14%,#3b3c40 30%,#2f3033 60%,#3a3b3e 100%)}
  .top-nav{top:52px;left:18px;right:18px;display:flex;justify-content:space-between;font-size:7.5px}
  .top-nav span{display:flex;align-items:center;gap:4px}
  .brand-word{font-weight:800;color:var(--red);line-height:1;white-space:nowrap}
  .picker .brand-word{top:143px;left:13px;font-size:21px;letter-spacing:.8px}
  .tagline{top:179px;left:13px;width:172px;font-weight:800;font-style:italic;font-size:10.4px;line-height:12.6px}
  .select-label{top:318px;left:0;width:100%;text-align:center;font-weight:700;font-size:8.5px}
  .division-btn{left:13px;width:181px;height:27px;display:flex;align-items:center;justify-content:center;font-size:8.5px;border:1px solid var(--white);color:var(--white)}
  .division-btn.active{background:var(--red);border-color:var(--red);color:#5a0a0d}

  /* Division page */
  .site-header{top:0;left:0;width:100%;height:48px;background:var(--screen)}
  .division .brand-word{top:17px;left:13px;font-size:11px;letter-spacing:.5px}
  .menu-icon{top:18px;left:179px}
  .division-hero{top:48px;left:0;width:100%;height:190px;background:linear-gradient(180deg,#55565b,#46474b 50%,#3c3d41)}
  .division-title{top:130px;left:14px;font-weight:700;font-size:22px}
  .about-text{top:326px;left:13px;width:184px;font-size:10.7px;line-height:12.6px}
  .video-thumb{top:408px;left:13px;width:181px;height:102px;border-radius:6px;background:linear-gradient(180deg,#6b6e70,#55585a 60%,#454749)}
  .play-btn{top:446px;left:96px}
  .play-label{top:464px;left:0;width:100%;text-align:center;font-size:8.5px}

  /* Leadership */
  .leader-card{left:28px;width:151px;height:191px;border-radius:6px;overflow:hidden}
  .leader-card .portrait{position:absolute;inset:0}
  .leader-info{position:absolute;left:9px;top:132px;width:133px;height:50px;background:var(--white);color:var(--ink);padding:8px 0 0 18px}
  .leader-info h3{font-size:8.5px;font-weight:600;line-height:10px}
  .leader-info p{font-size:7.5px;line-height:11px}
  .leader-info a{font-size:6.3px;color:var(--red);text-decoration:underline;line-height:13px}
  .leader-info a::after{content:" \2197";text-decoration:none;font-size:5px;display:inline-block;margin-left:3px;color:var(--ink)}

  /* Services */
  .services-bg{inset:0;background:linear-gradient(180deg,#55575b 0%,#3b3c40 25%,#323337 60%,#3f4044 100%)}
  .service-card{left:14px;width:181px;background:var(--white);border-radius:6px;overflow:hidden;color:var(--ink)}
  .service-card .photo{height:100px}
  .service-card .body{padding:9px 17px 0 18px}
  .service-card h3{font-size:8.6px;font-weight:600;line-height:10px;margin-top:1px}
  .service-card p{font-size:7.2px;line-height:9px;margin-top:9px}
  .service-card ul{font-size:7.2px;line-height:9px;margin-top:8px;list-style:none}
  .service-card li::before{content:"•";margin:0 5px 0 4px}
  .learn-more{position:absolute;left:18px;width:146px;height:20px;border:1px solid var(--red);color:var(--red);font-size:8.5px;display:flex;align-items:center;justify-content:center;gap:7px}

  /* Safety */
  .safety-intro{top:84px;left:13px;width:186px;font-size:10.8px;line-height:12.7px}
  .accordion{left:13px;width:181px;border:1.5px solid var(--red);border-radius:6px;font-size:8.5px;color:var(--white)}
  .accordion .head{display:flex;align-items:center;justify-content:space-between;padding:0 9px 0 17px;height:100%}
  .accordion.open{background:var(--white);color:var(--ink)}
  .accordion.open .head{height:30px;border-bottom:1px solid #e3e3e3;box-shadow:0 2px 3px rgba(0,0,0,.08)}
  .accordion.open ul{font-size:7.2px;line-height:9px;padding:16px 12px 0 28px}
  .careers{top:443px;left:0;width:100%;height:73px;background:var(--paper);color:var(--ink);padding:22px 14px 0 13px;font-size:10.8px;line-height:12.7px}
  .careers a{color:var(--ink);text-decoration:underline}
  .fleet-photo{top:516px;left:0;width:100%;height:111px;background:linear-gradient(180deg,#8c8f8c,#6e716d 55%,#5b5d58)}
  .contact{top:627px;left:0;width:100%;height:214px;background:var(--deep-red)}
  .contact .section-heading{position:absolute;top:55px;color:var(--white)}
  .contact-line{position:absolute;left:13px;display:flex;align-items:flex-start;gap:9px;font-size:7.8px;letter-spacing:1.2px;line-height:10px;white-space:nowrap}
  .contact-line.email{letter-spacing:.6px}
</style>
</head>
<body>

<div class="board-brand">MARLOWVANE</div>
<h1 class="board-title">Landing Page Mobile View</h1>

<!-- Division picker -->
<section class="phone picker" style="left:47px;top:49px;height:495px">
  <div class="hero-photo" role="img" aria-label="Aerial view of a small town with a crane truck"></div>
  <nav class="top-nav">
    <span>
      <svg width="6" height="8" viewBox="0 0 6 8"><path d="M5 1 2 4l3 3" fill="none" stroke="#fff" stroke-width="1.2"/></svg>Our Mission</span>
    <span>Our Vision
      <svg width="6" height="8" viewBox="0 0 6 8"><path d="M1 1l3 3-3 3" fill="none" stroke="#fff" stroke-width="1.2"/></svg></span>
  </nav>
  <div class="brand-word">MARLOWVANE</div>
  <p class="tagline">Delivering safe, reliable aerial access and maintenance services to Oil&amp;Gas, Construction, Utility, &amp; Renewable energy industries.</p>
  <p class="select-label">Select Division:</p>
  <a class="division-btn active" style="top:337px">Aerial Access</a>
  <a class="division-btn" style="top:373px">Geotechnical Drilling</a>
  <a class="division-btn" style="top:409px">Renewable Energy Services</a>
</section>

<!-- Division page -->
<section class="phone division" style="left:47px;top:581px;height:568px">
  <header class="site-header"></header>
  <div class="brand-word">MARLOWVANE</div>
  <svg class="menu-icon" width="14" height="11" viewBox="0 0 14 11"><path d="M0 1h14M0 5.5h14M0 10h14" stroke="#fff" stroke-width="1.4"/></svg>
  <div class="division-hero" role="img" aria-label="Aerial view of a town with a company crane truck"></div>
  <h2 class="division-title">Aerial Access</h2>
  <h2 class="section-heading start" style="top:294px">ABOUT</h2>
  <p class="about-text">Marlowvane is a full-service wind energy service provider specializing in blade access and repair, service and maintenance, and trouble shooting on most wind turbine platforms.</p>
  <div class="video-thumb" role="img" aria-label="Video still of an aerial platform truck"></div>
  <svg class="play-btn" width="14" height="14" viewBox="0 0 14 14"><circle cx="7" cy="7" r="7" fill="#fff"/><path d="M5.5 4.2v5.6L10 7z" fill="#2d2d32"/></svg>
  <p class="play-label">Play Video</p>
</section>

<!-- Leadership -->
<section class="phone" style="left:299px;top:216px;height:933px">
  <h2 class="section-heading" style="top:51px">OUR LEADERSHIP</h2>

  <article class="leader-card" style="top:83px">
    <div class="portrait" role="img" aria-label="Portrait of the company founder" style="background:linear-gradient(180deg,#b8b7b0,#8d8c86 45%,#2f3033)"></div>
    <div class="leader-info"><h3>Alden Prewitt</h3><p>Position</p><a>Read biography</a></div>
  </article>
  <article class="leader-card" style="top:283px">
    <div class="portrait" role="img" aria-label="Portrait of the vice president" style="background:linear-gradient(180deg,#3c48b8,#4a55c6 50%,#2b3270)"></div>
    <div class="leader-info"><h3>Dorian Halvey</h3><p>Vice President</p><a>Read biography</a></div>
  </article>
  <article class="leader-card" style="top:483px">
    <div class="portrait" role="img" aria-label="Portrait of a team leader" style="background:linear-gradient(180deg,#3a2a1c,#8a6a44 45%,#5d4429)"></div>
    <div class="leader-info"><h3>Wes Tannard</h3><p>Position</p><a>Read biography</a></div>
  </article>
  <article class="leader-card" style="top:684px">
    <div class="portrait" role="img" aria-label="Portrait of the VP of operations" style="background:linear-gradient(180deg,#2a2a2c,#3a3a3e 50%,#2c2c30)"></div>
    <div class="leader-info"><h3>Elias Okafor</h3><p>VP of Operations</p><a>Read biography</a></div>
  </article>
</section>

<!-- Services -->
<section class="phone" style="left:550px;top:431px;height:718px">
  <div class="services-bg" role="img" aria-label="Faded aerial photo of a crane yard"></div>
  <h2 class="section-heading light" style="top:58px">SERVICES</h2>

  <article class="service-card" style="top:84px;height:182px">
    <div class="photo" role="img" aria-label="White blade basket truck on a gravel yard" style="background:linear-gradient(180deg,#9aa3a8,#6f7470 55%,#5a554c)"></div>
    <div class="body">
      <h3>Blade basket</h3>
      <p>Lorem ipsum dolor sit amet consectetur. Lectus eget eget et fringilla et vel sagittis.</p>
    </div>
    <a class="learn-more" style="top:154px">Learn more <svg width="5" height="8" viewBox="0 0 5 8"><path d="M1 1l3 3-3 3" fill="none" stroke="#ec1c24" stroke-width="1.2"/></svg></a>
  </article>

  <article class="service-card" style="top:276px;height:192px">
    <div class="photo" role="img" aria-label="Truck mounted aerial work platform in a parking lot" style="background:linear-gradient(180deg,#5f93d6,#a9b3bb 55%,#6e7276)"></div>
    <div class="body">
      <h3>Truck mounted aerial work platforms</h3>
      <p>We own and maintain a fleet of truck mounted aerial work platforms</p>
    </div>
    <a class="learn-more" style="top:164px">Learn more <svg width="5" height="8" viewBox="0 0 5 8"><path d="M1 1l3 3-3 3" fill="none" stroke="#ec1c24" stroke-width="1.2"/></svg></a>
  </article>

  <article class="service-card" style="top:477px;height:183px">
    <div class="photo" role="img" aria-label="Crane truck parked on a forest road" style="background:linear-gradient(180deg,#5f7048,#7b8460 45%,#8a857a)"></div>
    <div class="body">
      <h3>Our fleet</h3>
      <ul><li>Unit 12 RT 38m</li><li>Unit 19 HX 61m</li></ul>
    </div>
    <a class="learn-more" style="top:155px">Learn more <svg width="5" height="8" viewBox="0 0 5 8"><path d="M1 1l3 3-3 3" fill="none" stroke="#ec1c24" stroke-width="1.2"/></svg></a>
  </article>
</section>

<!-- Safety, careers, contact -->
<section class="phone" style="left:803px;top:300px;height:849px">
  <h2 class="section-heading start" style="top:51px">SAFETY</h2>
  <p class="safety-intro">Safety is at the forefront of everything we do. Our mission is to create a safe work place through the following steps</p>

  <div class="accordion" style="top:152px;height:37px"><div class="head"><span>Safe Work Processes<br>And procedures</span><svg width="8" height="5" viewBox="0 0 8 5"><path d="M1 1l3 3 3-3" fill="none" stroke="#ec1c24" stroke-width="1.2"/></svg></div></div>
  <div class="accordion" style="top:199px;height:30px"><div class="head"><span>Company Culture</span><svg width="8" height="5" viewBox="0 0 8 5"><path d="M1 1l3 3 3-3" fill="none" stroke="#ec1c24" stroke-width="1.2"/></svg></div></div>
  <div class="accordion open" style="top:239px;height:108px">
    <div class="head"><span>Training and Development</span><svg width="8" height="5" viewBox="0 0 8 5"><path d="M1 4l3-3 3 3" fill="none" stroke="#ec1c24" stroke-width="1.2"/></svg></div>
    <ul>
      <li>We have regular training modules that all of our team is required to complete covering a wide range of safety topics.</li>
      <li>Platform specific training</li>
      <li>First aid for all field techs</li>
    </ul>
  </div>
  <div class="accordion" style="top:358px;height:30px"><div class="head"><span>Work Gear</span><svg width="8" height="5" viewBox="0 0 8 5"><path d="M1 1l3 3 3-3" fill="none" stroke="#ec1c24" stroke-width="1.2"/></svg></div></div>

  <div class="careers">We are always looking for skilled operators to join our team. <a>Email: career@marlowvane-example.com</a></div>
  <div class="fleet-photo" role="img" aria-label="Company crane truck parked outdoors"></div>
  <div class="contact">
    <h2 class="section-heading start">CONTACT</h2>
    <div class="contact-line" style="top:90px">
      <svg width="11" height="14" viewBox="0 0 11 14"><path d="M5.5 0A5.5 5.5 0 0 0 0 5.5C0 9.5 5.5 14 5.5 14S11 9.5 11 5.5A5.5 5.5 0 0 0 5.5 0Zm0 7.6a2.1 2.1 0 1 1 0-4.2 2.1 2.1 0 0 1 0 4.2Z" fill="#fff"/></svg>
      <span>218 Ridgeline Road Elmbrook<br>AB T0X-4K2</span>
    </div>
    <div class="contact-line email" style="top:127px">
      <svg width="15" height="11" viewBox="0 0 15 11"><rect width="15" height="11" rx="1" fill="#fff"/><path d="M1 1.5l6.5 4.5L14 1.5" fill="none" stroke="#8b2327" stroke-width="1.3"/></svg>
      <span style="line-height:12px">info@marlowvane-example.com</span>
    </div>
  </div>
</section>

</body>
</html>
```